Eyecatching Carpentry Business card

I need a business card designed for myself, my company name is Lewis Dunmore Carpentry.
I am based on the south coast of England and I do all aspects of carpentry, including;
skirting
Architraves
kitchens
roof construction
flooring
doors
loft conversions
decking
windows
I currently have no company logo or letter head so I leave all design ideas to designers.
All I ask is that it looks professional and modern.
A logo may be incorporated as well.
My contact details should be on the back, telephone and email.

```html
<!DOCTYPE html>
<html lang="en">
<head>
<meta charset="utf-8">
<title>Lewis Dunmore Carpentry – Business Card</title>
<link href="https://fonts.googleapis.com/css2?family=Marcellus&display=swap" rel="stylesheet">
<style>
  :root {
    --backdrop: #ececec;
    --card-cream: #f7f5ef;
    --card-cream-edge: #e9e5db;
    --walnut: #6e2d16;
    --walnut-deep: #5a2310;
    --walnut-light: #8a3d1f;
    --brass: #b58a4c;
    --brass-light: #e2c48e;
    --text-light: #fbf4ee;
  }
  * { margin: 0; padding: 0; box-sizing: border-box; }
  html, body {
    width: 1200px;
    height: 825px;
    overflow: hidden;
    background: var(--backdrop);
    font-family: "Marcellus", "Times New Roman", serif;
  }
  .sheet {
    width: 1200px;
    height: 825px;
    display: flex;
    align-items: center;
    justify-content: center;
    gap: 60px;
  }
  .card {
    width: 520px;
    height: 300px;
    border-radius: 18px;
    position: relative;
    box-shadow: 0 6px 18px rgba(0, 0, 0, 0.12);
  }

  /* Front */
  .card--front {
    background: linear-gradient(135deg, var(--card-cream) 0%, #ffffff 55%, var(--card-cream-edge) 100%);
    display: flex;
    flex-direction: column;
    align-items: center;
    justify-content: center;
    color: var(--walnut);
  }
  .brand {
    display: flex;
    align-items: center;
    gap: 14px;
  }
  .brand__dot {
    width: 16px;
    height: 16px;
    border-radius: 50%;
    background: var(--brass);
  }
  .brand__name {
    font-size: 44px;
    line-height: 1;
    letter-spacing: 0.5px;
  }
  .brand__trade {
    margin-top: 10px;
    font-size: 18px;
    letter-spacing: 9px;
    text-transform: uppercase;
    padding-left: 30px;
  }

  /* Back */
  .card--back {
    background: linear-gradient(160deg, var(--walnut-light) 0%, var(--walnut) 45%, var(--walnut-deep) 100%);
    color: var(--text-light);
  }
  .house-mark {
    position: absolute;
    left: 200px;
    top: 26px;
    width: 84px;
    height: 40px;
    border-radius: 3px;
    background: linear-gradient(180deg, var(--brass-light), var(--brass));
  }
  .services {
    position: absolute;
    left: 60px;
    top: 82px;
    width: 240px;
    list-style: none;
    text-align: center;
    font-size: 19px;
    line-height: 22px;
  }
  .contact {
    position: absolute;
    right: 34px;
    bottom: 34px;
    font-size: 17px;
    line-height: 24px;
    text-align: left;
  }
  .contact__phone {
    display: flex;
    align-items: center;
    gap: 8px;
  }
  .contact__phone svg { width: 18px; height: 18px; }
</style>
</head>
<body>
  <main class="sheet">
    <section class="card card--front" aria-label="Card front">
      <div class="brand">
        <span class="brand__dot"></span>
        <h1 class="brand__name">Lewis Dunmore</h1>
      </div>
      <p class="brand__trade">Carpentry</p>
    </section>

    <section class="card card--back" aria-label="Card back">
      <div class="house-mark" role="img" aria-label="Gold house roof emblem"></div>
      <ul class="services">
        <li>kitchens</li>
        <li>roof construction</li>
        <li>flooring</li>
        <li>doors</li>
        <li>loft conversions</li>
        <li>decking</li>
        <li>windows</li>
      </ul>
      <div class="contact">
        <p>41 south coast UK</p>
        <p class="contact__phone">
          <svg viewBox="0 0 20 20" aria-hidden="true">
            <circle cx="10" cy="10" r="8.5" fill="none" stroke="currentColor" stroke-width="1.5"/>
            <path d="M7 5.5c-.8.3-1.3 1-1.1 2 .5 2.8 2.8 5.3 5.6 6.3 1 .3 1.8-.1 2.2-.9l-1.7-1.4-1.1.6c-1.2-.6-2.1-1.6-2.6-2.8l.7-1z" fill="currentColor"/>
          </svg>
          555-018-2046
        </p>
      </div>
    </section>
  </main>
</body>
</html>
```